Poster Design Needed for Events

I would like a poster designed for our events.. We do evenings of Mediumship/Psychic at theatres ect.. the image below would need to be included... I Would also like the following wording to be included... "Renowned Spiritualist Medium Dafydd Pemberton Presents Whispers From the Lighthouse" There will also Need to be a Place on the poster where event details can be put.. as they Change everytime.. Colours for background maybe blue,, maybe Clouds ect..

```html
<!DOCTYPE html>
<html lang="en">
<head>
<meta charset="utf-8">
<title>Dafydd Pemberton — Whispers From the Lighthouse</title>
<link rel="stylesheet" href="https://fonts.googleapis.com/css2?family=League+Gothic&family=Ubuntu:wght@400;500&display=swap">
<style>
  :root {
    --ink: #000000;
    --frame: #e8e8e8;
    --headline: #c9c9c9;
    --text: #ffffff;
    --accent: #b592dc;
    --glow: #3a2540;
  }
  html, body {
    margin: 0;
    padding: 0;
    background: var(--ink);
    overflow: hidden;
  }
  .poster {
    position: relative;
    width: 849px;
    height: 1200px;
    background: var(--ink);
    overflow: hidden;
    font-family: "Ubuntu", sans-serif;
    color: var(--text);
  }
  .poster-frame {
    position: absolute;
    inset: 6px;
    border: 1px solid var(--frame);
    pointer-events: none;
  }
  .portrait {
    position: absolute;
    left: 296px;
    top: 32px;
    width: 540px;
    height: 956px;
    background:
      radial-gradient(circle at 81% 63%, rgba(255,255,255,0.55) 0, rgba(220,200,235,0.18) 40px, transparent 110px),
      radial-gradient(ellipse at 45% 30%, #6a5566 0, #3c2c3c 30%, transparent 65%),
      radial-gradient(ellipse at 60% 75%, var(--glow) 0, #1a1220 55%, transparent 85%),
      linear-gradient(90deg, #000 0, #140d16 30%, #1e1422 70%, #000 100%);
  }
  .headline {
    position: absolute;
    left: 24px;
    width: 412px;
    top: 56px;
    margin: 0;
    display: flex;
    flex-direction: column;
    align-items: flex-end;
    gap: 6px;
    font-family: "League Gothic", "Oswald", sans-serif;
    font-weight: 400;
    text-transform: uppercase;
    color: var(--headline);
    text-align: right;
  }
  .headline span { display: block; line-height: 0.82; white-space: nowrap; }
  .headline .intro { font-size: 112px; }
  .headline .name { font-size: 126px; }
  .headline .presents { font-size: 108px; margin-top: 10px; }
  .headline .title { font-size: 112px; }
  .rule {
    position: absolute;
    left: 7px;
    right: 7px;
    top: 989px;
    height: 2px;
    background: var(--frame);
  }
  .event-details {
    position: absolute;
    left: 0;
    right: 0;
    top: 1004px;
    text-align: center;
  }
  .venue {
    margin: 0;
    font-size: 26px;
    font-weight: 400;
    font-variant: small-caps;
    letter-spacing: 1px;
    line-height: 1.1;
  }
  .address { margin: 2px 0 0; font-size: 18px; line-height: 1.2; }
  .when {
    margin: 14px 0 0;
    font-size: 21px;
    line-height: 1.2;
  }
  .when .accent { font-size: 31px; }
  .when .sep { font-size: 14px; margin: 0 18px; vertical-align: 4px; }
  .accent { color: var(--accent); font-weight: 500; }
  .booking { margin: 14px 0 0; font-size: 21px; line-height: 1.2; }
  .booking .price { font-size: 24px; font-weight: 500; }
</style>
</head>
<body>
<main class="poster">
  <div class="portrait" role="img" aria-label="Portrait photograph of the medium in a dark suit reaching out with a glowing light in his open hand"></div>

  <h1 class="headline">
    <span class="intro">Renowned</span>
    <span class="intro">Spiritualist</span>
    <span class="intro">Medium</span>
    <span class="name">Dafydd</span>
    <span class="name">Pemberton</span>
    <span class="presents">Presents</span>
    <span class="title">Whispers</span>
    <span class="title">From the</span>
    <span class="title">Lighthouse</span>
  </h1>

  <div class="rule"></div>

  <section class="event-details">
    <h2 class="venue">Penarth Road Community Hall</h2>
    <p class="address">Rowan Street, CARDIFF, CF 11 4QT</p>
    <p class="when">
      Friday July <span class="accent">29th 2016</span><span class="sep">&#9830;</span>Doors open at <span class="accent">7pm</span><span class="sep">&#9830;</span>Tickets <span class="accent">£9</span>
    </p>
    <p class="booking">
      Tickets <span class="price">£7</span> in advance available from<br>
      <span class="accent">lighthousemedium.co.uk</span> or by calling <span class="accent">07700900461</span>
    </p>
  </section>

  <div class="poster-frame"></div>
</main>
</body>
</html>
```